Create a step-by-step donors pamphlet for TOLVEK church

I am looking to get a professionally design pamphlet that gives our donors easy steps to set up reoccurring donation through our give platform.

The ideal design should look professional and creative. No templates or weak AIs.

I've provided church logos and a text file which contains the content of the pamphlet we are trying to make.

Font styles to use
Sans Serif

Requirements
Must have
• Good branding

```html
<!DOCTYPE html>
<html lang="en">
<head>
<meta charset="utf-8">
<title>TOLVEK Church – Recurring Donor Pamphlet</title>
<link rel="stylesheet" href="https://fonts.googleapis.com/css2?family=Oswald:wght@400;500;600;700&family=Roboto:wght@400;500;700&display=swap">
<style>
  :root {
    --bg: #d9d9d9;
    --black: #111111;
    --black-soft: #1c1c1c;
    --white: #ffffff;
    --paper: #f7f7f5;
    --orange: #ea7a2c;
    --orange-deep: #d8612a;
    --flame-yellow: #f8b23a;
    --flame-red: #c73b1c;
    --ash: #3a3a3a;
    --grey-text: #bdbdbd;
    --dark-text: #222222;
  }
  * { box-sizing: border-box; margin: 0; padding: 0; }
  html, body { width: 1200px; height: 900px; overflow: hidden; }
  body {
    background: var(--bg);
    font-family: "Roboto", Arial, sans-serif;
    position: relative;
  }
  .pamphlet {
    position: absolute;
    left: 60px; top: 50px;
    width: 1080px; height: 800px;
    display: flex;
  }
  .panel { width: 360px; height: 800px; position: relative; overflow: hidden; }

  /* Cover panel */
  .panel--cover { background: var(--black); color: var(--white); }
  .flame {
    position: absolute;
    background: radial-gradient(ellipse at 50% 85%, var(--flame-yellow) 0%, var(--orange) 45%, var(--flame-red) 80%, transparent 100%);
  }
  .flame--small { left: 40px; top: 40px; width: 90px; height: 90px; border-radius: 50% 50% 45% 45% / 60% 60% 40% 40%; }
  .flame--large { left: 30px; top: 410px; width: 300px; height: 170px; border-radius: 55% 55% 40% 40% / 70% 70% 30% 30%; }
  .cover-title {
    position: absolute; left: 36px; top: 150px;
    font-family: "Oswald", Impact, sans-serif; font-weight: 600;
    font-size: 64px; line-height: 0.98; text-transform: uppercase;
    letter-spacing: -0.5px;
  }
  .cover-brand {
    position: absolute; left: 36px; top: 640px;
    font-family: "Oswald", Impact, sans-serif; font-weight: 700;
    font-size: 50px; line-height: 1;
  }
  .cover-brand-sub {
    position: absolute; left: 40px; top: 700px;
    font-size: 11px; letter-spacing: 1px; text-transform: uppercase; color: var(--orange);
  }
  .cover-tagline {
    position: absolute; left: 36px; top: 750px;
    font-size: 12px; letter-spacing: 1px; text-transform: uppercase;
  }

  /* Middle panel */
  .panel--inside { background: var(--black-soft); color: var(--white); padding: 52px 34px 0; }
  .eyebrow {
    font-family: "Oswald", sans-serif; font-weight: 600; font-size: 16px;
    color: var(--orange); text-transform: uppercase; letter-spacing: 0.5px;
  }
  .inside-title {
    margin-top: 10px;
    font-family: "Oswald", Impact, sans-serif; font-weight: 500;
    font-size: 52px; line-height: 1.02; text-transform: uppercase;
  }
  .intro { margin-top: 28px; font-size: 13px; line-height: 1.45; color: var(--white); }
  .section-label {
    margin-top: 30px;
    font-family: "Oswald", sans-serif; font-weight: 500; font-size: 18px;
    color: var(--orange); text-transform: uppercase;
  }
  .steps { list-style: none; margin-top: 18px; }
  .step { display: flex; align-items: center; gap: 16px; margin-bottom: 30px; }
  .step-num {
    flex: none; width: 36px; height: 36px; border-radius: 50%;
    background: var(--orange); color: var(--white);
    font-family: "Oswald", sans-serif; font-size: 20px;
    display: flex; align-items: center; justify-content: center;
  }
  .step-text { font-size: 12px; line-height: 1.45; }
  .web {
    position: absolute; left: 34px; bottom: 42px;
    font-size: 14px; color: var(--orange);
  }

  /* Right panel */
  .panel--steps { background: var(--paper); color: var(--dark-text); }
  .steps-head { background: var(--orange); height: 275px; padding: 50px 30px 0; position: relative; }
  .steps-title {
    font-family: "Roboto", sans-serif; font-weight: 500; font-size: 26px;
    line-height: 1.35; color: var(--black);
  }
  .steps-sub { margin-top: 22px; width: 200px; font-size: 12px; line-height: 1.4; color: var(--white); }
  .rock {
    position: absolute; right: 0; top: 180px; width: 90px; height: 150px;
    background: linear-gradient(160deg, var(--ash), var(--black));
    clip-path: polygon(60% 0, 100% 0, 100% 100%, 0 100%, 20% 55%);
  }
  .all-set {
    position: absolute; left: 30px; top: 295px; width: 280px; height: 110px;
    background: var(--orange); border-radius: 12px; border: 3px solid #f0a56f;
    display: flex; align-items: center; justify-content: center; text-align: center;
    font-family: "Oswald", sans-serif; font-size: 24px; line-height: 1.2;
    color: var(--white); text-transform: uppercase;
  }
  .steps--right { position: absolute; left: 30px; top: 435px; width: 300px; margin: 0; }
  .steps--right .step { align-items: flex-start; margin-bottom: 22px; }
  .step-heading {
    font-family: "Oswald", sans-serif; font-weight: 500; font-size: 15px;
    text-transform: uppercase; color: var(--black);
  }
  .steps--right .step-text { font-size: 11px; color: #555; margin-top: 2px; }
  .flame--corner { left: 170px; top: 680px; width: 190px; height: 140px; border-radius: 50% 50% 0 0 / 80% 80% 0 0; }
  .flame--corner-left { left: 0; top: 700px; width: 120px; height: 120px; border-radius: 50% 50% 0 0 / 80% 80% 0 0; }
</style>
</head>
<body>
  <main class="pamphlet">
    <section class="panel panel--cover">
      <div class="flame flame--small" role="img" aria-label="Small flame illustration"></div>
      <h1 class="cover-title">Are you a recurring donor yet?</h1>
      <div class="flame flame--large" role="img" aria-label="Large flame illustration"></div>
      <div class="cover-brand">TOLVEK</div>
      <div class="cover-brand-sub">A house of worship</div>
      <div class="cover-tagline">A welcome to all nations</div>
    </section>

    <section class="panel panel--inside">
      <p class="eyebrow">Partner with TOLVEK</p>
      <h2 class="inside-title">Be a recurring donator</h2>
      <p class="intro">Setting up a recurring gift is simple. It keeps our ministry strong all year long.</p>
      <h3 class="section-label">Giving instructions</h3>
      <ol class="steps">
        <li class="step"><span class="step-num">1</span><p class="step-text">Open the giving page on our website or app.</p></li>
        <li class="step"><span class="step-num">2</span><p class="step-text">Sign in or create your free donor account.</p></li>
        <li class="step"><span class="step-num">3</span><p class="step-text">Choose the fund you would like to support.</p></li>
        <li class="step"><span class="step-num">4</span><p class="step-text">Enter your amount and payment details.</p></li>
      </ol>
      <p class="web">www.tolvekchurch.org</p>
    </section>

    <section class="panel panel--steps">
      <header class="steps-head">
        <h2 class="steps-title">Faithful Recurring<br>Donating Patrons</h2>
        <p class="steps-sub">Give faithfully each month and help our church grow.</p>
      </header>
      <div class="rock" role="img" aria-label="Dark rock illustration"></div>
      <div class="all-set">That's it —<br>you're all set!</div>
      <ol class="steps steps--right">
        <li class="step"><span class="step-num">1</span><div><p class="step-heading">How to access the app</p><p class="step-text">Download the app from your store and sign in.</p></div></li>
        <li class="step"><span class="step-num">2</span><div><p class="step-heading">Enter gift amount</p><p class="step-text">Type the amount you wish to give.</p></div></li>
        <li class="step"><span class="step-num">3</span><div><p class="step-heading">Select recurring</p><p class="step-text">Pick weekly, monthly or yearly giving.</p></div></li>
        <li class="step"><span class="step-num">4</span><div><p class="step-heading">Click next</p><p class="step-text">Confirm your gift and you are done.</p></div></li>
      </ol>
      <div class="flame flame--corner-left" role="img" aria-label="Flame and rock illustration"></div>
      <div class="flame flame--corner" role="img" aria-label="Flame illustration"></div>
    </section>
  </main>
</body>
</html>
```